LoftHaven conversion company design.

Hi,

We specialise in attic/roof conversions to create more space. We have a logo design which we are happy with. We would like someone to design a wrap that will be suitable to be transferred onto a 2008 Corvan 300. This is our first car to be wrapped and is what we require a design for.

However, we would like to see a design that can be utilised on a KT Belozan, and 2021 Lundrelle Vantage van. (I understand the design would change to suit but I would like something that will still look similar when they are sat next to one another).

We have a white background on the car so that would need consideration.

We want something that is noticeable but looks professional.

We will also require are contact information on the design:

email: admin@lofthaven-example.com.au
Website: lofthaven-example.com.au
Tel: 1300748216
Social media icons- Snapvelo, Mingleroo, Boardwisp, Quorble

Please let me know if you require any further detail.

```html
<!DOCTYPE html>
<html lang="en">
<head>
<meta charset="utf-8">
<title>LoftHaven Vehicle Wrap</title>
<link rel="stylesheet" href="https://fonts.googleapis.com/css2?family=Montserrat:wght@500;600;700&display=swap">
<style>
  :root {
    --navy: #1f3243;
    --blue: #1e7bc4;
    --white: #ffffff;
    --faint: #d9dcdf;
    --page: #ffffff;
  }
  * { box-sizing: border-box; margin: 0; padding: 0; }
  html, body { width: 1200px; height: 1010px; overflow: hidden; background: var(--page); }
  body { font-family: "Montserrat", sans-serif; color: var(--navy); position: relative; }

  .wrap-panel { position: absolute; left: 50px; width: 1100px; }
  .wrap-panel svg { position: absolute; inset: 0; display: block; }
  .wrap-ute { top: 70px; height: 330px; }
  .wrap-van { top: 580px; height: 360px; }

  .layer { position: absolute; }

  .brand-name { font-weight: 700; color: var(--blue); letter-spacing: 0.5px; line-height: 1; }
  .brand-mark { display: inline-block; background: var(--navy); vertical-align: middle; }
  .tagline { font-weight: 600; color: var(--navy); letter-spacing: 0.2px; }
  .tagline-rule { height: 3px; background: var(--blue); }

  .phone { font-weight: 700; line-height: 1; letter-spacing: 1px; }
  .email { font-weight: 600; letter-spacing: 0.5px; }
  .website { font-weight: 600; color: var(--white); letter-spacing: 0.5px; }

  .social { display: flex; gap: 14px; }
  .social-item { display: flex; align-items: center; gap: 5px; font-weight: 600; }
  .social-dot { border-radius: 50%; flex: none; }

  /* ute */
  .wrap-ute .social { left: 90px; top: 160px; }
  .wrap-ute .social-item { font-size: 11px; color: var(--navy); }
  .wrap-ute .social-dot { width: 12px; height: 12px; background: var(--navy); }
  .wrap-ute .brand { left: 320px; top: 190px; width: 200px; text-align: center; }
  .wrap-ute .brand-name { font-size: 27px; }
  .wrap-ute .brand-mark { width: 12px; height: 12px; margin-right: 6px; }
  .wrap-ute .tagline { font-size: 9px; margin-top: 6px; }
  .wrap-ute .tagline-rule { width: 70px; margin: 5px auto 0; }
  .wrap-ute .contact { left: 790px; top: 135px; color: var(--white); }
  .wrap-ute .phone { font-size: 25px; }
  .wrap-ute .email { font-size: 14px; margin-top: 6px; }
  .wrap-ute .website { left: 360px; top: 290px; font-size: 18px; }

  /* van */
  .wrap-van .watermark { left: 560px; top: 140px; font-size: 66px; font-weight: 700; color: var(--faint); letter-spacing: 2px; }
  .wrap-van .brand { left: 680px; top: 95px; }
  .wrap-van .brand-name { font-size: 48px; }
  .wrap-van .brand-mark { width: 22px; height: 22px; margin-right: 10px; }
  .wrap-van .tagline { font-size: 15px; margin-top: 10px; margin-left: 30px; }
  .wrap-van .tagline-rule { width: 110px; margin: 6px 0 0 110px; }
  .wrap-van .contact { left: 260px; top: 208px; color: var(--navy); }
  .wrap-van .phone { font-size: 28px; }
  .wrap-van .email { font-size: 15px; margin-top: 6px; }
  .wrap-van .social { left: 670px; top: 250px; }
  .wrap-van .social-item { font-size: 13px; color: var(--white); }
  .wrap-van .social-dot { width: 16px; height: 16px; background: var(--white); }
  .wrap-van .website { left: 670px; top: 290px; font-size: 19px; }
</style>
</head>
<body>

<section class="wrap-panel wrap-ute" aria-label="Ute side wrap">
  <svg viewBox="0 0 1100 330" width="1100" height="330" aria-hidden="true">
    <rect class="panel-base" x="0" y="0" width="1100" height="330" fill="var(--white)"/>
    <polygon class="accent-stripe" points="0,262 600,262 730,80 790,80 660,280 0,280" fill="var(--blue)"/>
    <polygon class="base-band" points="0,280 660,280 790,80 1100,80 1100,330 0,330" fill="var(--navy)"/>
  </svg>

  <div class="layer social">
    <span class="social-item"><span class="social-dot"></span>Quorble</span>
    <span class="social-item"><span class="social-dot"></span>Snapvelo</span>
    <span class="social-item"><span class="social-dot"></span>Mingleroo</span>
    <span class="social-item"><span class="social-dot"></span>Boardwisp</span>
  </div>

  <div class="layer brand">
    <div class="brand-name"><span class="brand-mark"></span>LOFTHAVEN</div>
    <p class="tagline">Storage • Skylights • Conversions</p>
    <div class="tagline-rule"></div>
  </div>

  <div class="layer contact">
    <p class="phone">1300-74-82-16</p>
    <p class="email">admin@lofthaven-example.com.au</p>
  </div>

  <p class="layer website">Lofthaven-example.com.au</p>
</section>

<section class="wrap-panel wrap-van" aria-label="Van side wrap">
  <svg viewBox="0 0 1100 360" width="1100" height="360" aria-hidden="true">
    <rect class="panel-base" x="0" y="0" width="1100" height="360" fill="var(--white)"/>
    <polygon class="accent-stripe" points="0,292 560,292 650,200 1100,200 1100,216 662,216 575,310 0,310" fill="var(--blue)"/>
    <polygon class="base-band" points="0,310 575,310 662,216 1100,216 1100,360 0,360" fill="var(--navy)"/>
  </svg>

  <p class="layer watermark" aria-hidden="true">LOFTHAVEN</p>

  <div class="layer brand">
    <div class="brand-name"><span class="brand-mark"></span>LOFTHAVEN</div>
    <p class="tagline">Storage • Skylights • Conversions</p>
    <div class="tagline-rule"></div>
  </div>

  <div class="layer contact">
    <p class="phone">1300-74-82-16</p>
    <p class="email">admin@lofthaven-example.com.au</p>
  </div>

  <div class="layer social">
    <span class="social-item"><span class="social-dot"></span>Quorble</span>
    <span class="social-item"><span class="social-dot"></span>Snapvelo</span>
    <span class="social-item"><span class="social-dot"></span>Mingleroo</span>
    <span class="social-item"><span class="social-dot"></span>Boardwisp</span>
  </div>

  <p class="layer website">Lofthaven-example.com.au</p>
</section>

</body>
</html>
```